New Gold Anchor Cards

We are a high end restroom trailer company. Please see our website for our design and exactly what we do.
goldanchorrestrooms.example
See tan back ground on the website. We would like to use that as the background. Also we would like to add 1 or two photos of the interior of our restroom trailers to the back of the card.

Also we would like the business card adjustable since I need to buy for other employees in my business. Gordon Prewitt with cell 555-214-8037 and Curtis Halloway with cell 555-482-1953. All the other information is the same as mine.

Industry/Entity Type

It Company

Contact Information for Business Card

Denise Prewitt
(555) 617-2048 office
(555) 239-7714 cell
dee@goldanchorrestrooms.example
GoldAnchorRestrooms.example

```html
<!DOCTYPE html>
<html lang="en">
<head>
<meta charset="utf-8">
<title>Gold Anchor Business Cards</title>
<link rel="stylesheet" href="https://fonts.googleapis.com/css2?family=Cinzel:wght@600&family=Open+Sans:wght@400;600&display=swap">
<style>
  :root {
    --page: #ecebe8;
    --card-tan: #efe5d2;
    --card-tan-shade: #e2d4b8;
    --brand-blue: #1f6fb5;
    --band-grey: #4a4a4c;
    --ink-light: #ffffff;
    --photo-warm: #c9b48f;
    --photo-cool: #8f9aa3;
    --shadow: rgba(0, 0, 0, 0.18);
  }
  * { box-sizing: border-box; margin: 0; padding: 0; }
  html, body { width: 1200px; height: 828px; overflow: hidden; }
  body {
    background: var(--page);
    font-family: "Open Sans", Arial, sans-serif;
    position: relative;
  }
  .card {
    position: absolute;
    top: 260px;
    width: 540px;
    height: 309px;
    background: linear-gradient(180deg, var(--card-tan) 0%, var(--card-tan-shade) 100%);
    box-shadow: 0 6px 18px var(--shadow);
    overflow: hidden;
  }
  .card-front { left: 40px; }
  .card-back { left: 620px; }

  .brand {
    position: absolute;
    display: flex;
    align-items: center;
    gap: 12px;
    white-space: nowrap;
  }
  .brand-dot {
    width: 40px; height: 40px;
    border-radius: 50%;
    background: var(--brand-blue);
  }
  .brand-name {
    font-family: "Cinzel", Georgia, serif;
    font-weight: 600;
    font-size: 28px;
    color: var(--brand-blue);
    letter-spacing: 0.5px;
  }
  .card-front .brand { left: 50%; top: 48px; transform: translateX(-50%); }
  .card-back .brand { left: 60px; top: 78px; }

  .interior-photos {
    position: absolute;
    left: 50%;
    top: 128px;
    transform: translateX(-50%);
    display: flex;
    gap: 16px;
  }
  .interior-photo {
    width: 200px;
    height: 130px;
    border-radius: 4px;
  }
  .interior-photo.warm { background: linear-gradient(135deg, #d8c6a4 0%, var(--photo-warm) 100%); }
  .interior-photo.cool { background: linear-gradient(135deg, #b7bfc5 0%, var(--photo-cool) 100%); }

  .bands { position: absolute; inset: 0; width: 100%; height: 100%; }

  .contact {
    position: absolute;
    left: 318px;
    top: 192px;
    color: var(--ink-light);
    font-size: 10px;
    line-height: 1.5;
  }
  .contact-row { display: flex; align-items: center; gap: 6px; white-space: nowrap; }
  .contact-row svg { width: 10px; height: 10px; fill: var(--ink-light); flex: none; }
  .contact-address { padding-left: 16px; }
  .contact-label { opacity: 0.85; }

  .person {
    position: absolute;
    left: 34px;
    bottom: 30px;
    color: var(--ink-light);
  }
  .person-name { font-size: 15px; font-weight: 600; letter-spacing: 1px; text-transform: uppercase; }
  .person-title { font-size: 10px; letter-spacing: 1.5px; text-transform: uppercase; }
</style>
</head>
<body>
  <section class="card card-front" aria-label="Card front">
    <div class="brand">
      <span class="brand-dot"></span>
      <span class="brand-name">Gold Anchor</span>
    </div>
    <div class="interior-photos">
      <div class="interior-photo warm" role="img" aria-label="Photo of a restroom trailer interior with vanity and sink"></div>
      <div class="interior-photo cool" role="img" aria-label="Photo of a restroom trailer interior with stalls and lighting"></div>
    </div>
  </section>

  <section class="card card-back" aria-label="Card back">
    <svg class="bands" viewBox="0 0 540 309" preserveAspectRatio="none" aria-hidden="true">
      <defs>
        <linearGradient id="blueBand" x1="0" y1="0" x2="1" y2="1">
          <stop offset="0" stop-color="#3a9be0"/>
          <stop offset="1" stop-color="#1d74bd"/>
        </linearGradient>
      </defs>
      <path d="M0,186 C210,196 430,150 540,14 L540,309 L0,309 Z" fill="var(--band-grey)"/>
      <path d="M0,198 C215,210 440,166 540,36 L540,309 L0,309 Z" fill="url(#blueBand)"/>
    </svg>

    <div class="brand">
      <span class="brand-dot"></span>
      <span class="brand-name">Gold Anchor</span>
    </div>

    <div class="contact">
      <div class="contact-row">
        <svg viewBox="0 0 10 10"><path d="M5,0.5 C3.1,0.5 1.8,1.9 1.8,3.6 C1.8,6 5,9.5 5,9.5 C5,9.5 8.2,6 8.2,3.6 C8.2,1.9 6.9,0.5 5,0.5 Z M5,2.4 A1.2,1.2 0 1 1 5,4.8 A1.2,1.2 0 1 1 5,2.4 Z"/></svg>
        <span>218 Harbor Lane, Suite 4</span>
      </div>
      <div class="contact-address">Marlow, MD 20772</div>
      <div class="contact-row">
        <svg viewBox="0 0 10 10"><path d="M2,0.5 L3.8,0.5 L4.4,2.8 L3.2,3.8 C3.8,5.2 4.8,6.2 6.2,6.8 L7.2,5.6 L9.5,6.2 L9.5,8 C9.5,8.9 8.8,9.5 8,9.5 C4,9.2 0.8,6 0.5,2 C0.5,1.2 1.1,0.5 2,0.5 Z"/></svg>
        <span>(555) 617-2048 <span class="contact-label">office</span></span>
      </div>
      <div class="contact-row">
        <svg viewBox="0 0 10 10"><path d="M2.5,0.5 L7.5,0.5 L7.5,9.5 L2.5,9.5 Z M4,8 L6,8 L6,8.6 L4,8.6 Z" fill-rule="evenodd"/></svg>
        <span>(555) 239-7714 <span class="contact-label">cell</span></span>
      </div>
      <div class="contact-row">
        <svg viewBox="0 0 10 10"><path d="M0.5,2 L9.5,2 L9.5,8 L0.5,8 Z M0.5,2 L5,5.5 L9.5,2" stroke="#2e8fd6" stroke-width="0.8"/></svg>
        <span>dee@goldanchorrestrooms.example</span>
      </div>
      <div class="contact-row">
        <svg viewBox="0 0 10 10"><circle cx="5" cy="5" r="4.5"/></svg>
        <span>GoldAnchorRestrooms.example</span>
      </div>
    </div>

    <div class="person">
      <div class="person-name">Jordan Ellery</div>
      <div class="person-title">President</div>
    </div>
  </section>
</body>
</html>
```